Business Card Design

I'm a young beekeeper (22 years old) just starting out. I own and run 80 hives and would like to eventually build up to 1000. My aim is to run it in tandem with our family farm that is currently running sheep and beef. Unlike a number of honey companies on the East Coast (or the North Island, NZ) I am local and will expand onto the lease blocks that our family is also leasing. I want a simple plain logo/photo. The designer may wish to use one of the photos as a background outline or however they chose. The mountain is Aorangi and our farm borders one side of it.

Target Market(s)

From local land owners to wholesale honey buyers

Industry/Entity Type

Farm

Contact Information for Business Card

Pekeriu Honey
Manager Owner Manaia Brooks
email pekeriuhoney@tuimailbox.co.nz
mobile 0217394461

Requirements
Must have
• The details submitted. The brand Pekeriu Honey to be the main feature. The other details can be smaller.
Should not have
• Must not include a picture of a bee or hive. Use a modern font. Don't use koru but may incorporate poutama.

```html
<!DOCTYPE html>
<html lang="en">
<head>
<meta charset="utf-8">
<title>Pekeriu Honey – Business Card</title>
<link href="https://fonts.googleapis.com/css2?family=Archivo:wght@800&family=Roboto+Condensed:wght@300;400&display=swap" rel="stylesheet">
<style>
  :root {
    --stage: #e9ecec;
    --card: #ffffff;
    --honey-light: #ffd21f;
    --honey: #f7b500;
    --honey-deep: #eaa000;
    --ink: #1c1c1c;
    --ink-soft: #333333;
    --badge-green: #3f8f2a;
    --icon: #f08a1c;
  }
  html, body {
    margin: 0;
    width: 1200px;
    height: 1200px;
    overflow: hidden;
    background: var(--stage);
  }
  .card {
    position: absolute;
    left: 100px;
    top: 314px;
    width: 1000px;
    height: 572px;
    background: var(--card);
    box-shadow: 0 10px 30px rgba(0,0,0,0.18);
    overflow: hidden;
  }
  .honey-band {
    position: absolute;
    left: 0;
    top: 0;
    width: 1000px;
    height: 170px;
    background: linear-gradient(180deg, var(--honey-light) 0%, var(--honey) 65%, var(--honey-deep) 100%);
  }
  .brand {
    position: absolute;
    left: 70px;
    top: 300px;
    width: 340px;
    display: flex;
    align-items: center;
    gap: 16px;
  }
  .brand-dot {
    width: 40px;
    height: 40px;
    border-radius: 50%;
    background: var(--badge-green);
    flex: none;
  }
  .brand-name {
    font-family: "Archivo", sans-serif;
    font-weight: 800;
    font-size: 40px;
    line-height: 1.05;
    color: var(--ink);
  }
  .details {
    position: absolute;
    left: 470px;
    top: 250px;
  }
  .person-name {
    font-family: "Archivo", sans-serif;
    font-weight: 800;
    font-size: 30px;
    color: var(--ink);
    margin: 0;
  }
  .person-role {
    font-family: "Roboto Condensed", sans-serif;
    font-weight: 300;
    font-size: 30px;
    color: var(--ink-soft);
    margin: 2px 0 34px;
  }
  .contact {
    list-style: none;
    margin: 0;
    padding: 0 0 0 34px;
    font-family: "Roboto Condensed", sans-serif;
    font-weight: 300;
    font-size: 26px;
    color: var(--ink-soft);
  }
  .contact li {
    display: flex;
    align-items: center;
    gap: 12px;
    margin-bottom: 16px;
  }
  .contact-icon {
    width: 20px;
    height: 20px;
    flex: none;
  }
</style>
</head>
<body>
  <div class="card">
    <div class="honey-band" role="img" aria-label="Honey-coloured decorative band along the top of the card"></div>

    <div class="brand">
      <span class="brand-dot"></span>
      <span class="brand-name">Pekeriu Honey</span>
    </div>

    <div class="details">
      <h1 class="person-name">Manaia Brooks</h1>
      <p class="person-role">Owner</p>
      <ul class="contact">
        <li>
          <svg class="contact-icon" viewBox="0 0 20 20" aria-hidden="true">
            <circle cx="10" cy="10" r="10" fill="var(--icon)"/>
            <rect x="5" y="6.5" width="10" height="7" rx="1" fill="#fff"/>
            <path d="M5.5 7L10 10.5L14.5 7" stroke="var(--icon)" stroke-width="1.2" fill="none"/>
          </svg>
          pekeriuhoney@tuimailbox.co.nz
        </li>
        <li>
          <svg class="contact-icon" viewBox="0 0 20 20" aria-hidden="true">
            <circle cx="10" cy="10" r="10" fill="var(--icon)"/>
            <rect x="7" y="4.5" width="6" height="11" rx="1.2" fill="#fff"/>
            <circle cx="10" cy="13.5" r="0.8" fill="var(--icon)"/>
          </svg>
          0217394461
        </li>
      </ul>
    </div>
  </div>
</body>
</html>
```